Business Card Design

My company is an online based training service targeted at individuals who want to learn how to consistently make money at online tournament poker.

The training takes place online using skype and is extremely easy to use.

Final design should communicate that my business offers online tournament poker coaching from one of the most successful online tournament poker players in Scotland and the UK.

Further information can be found @ http://www.mendmyhand.net/

Industry/Entity Type

Training

Contact Information for Business Card

- 'Learn from one of the best online tournament poker players in Scotland and the UK' (or something similar)
- Previous winnings
Reference: http://www.mendmyhand.net/

Requirements
Must have
• MendMyHand.net
Nice to have
• A similar look or feel to my website (http://www.mendmyhand.net/)

```html
<!DOCTYPE html>
<html lang="en">
<head>
<meta charset="utf-8">
<title>Ardmore Coaching – Business Card</title>
<link href="https://fonts.googleapis.com/css2?family=Arimo:wght@400&display=swap" rel="stylesheet">
<style>
  :root {
    --ink: #262626;
    --gold: #fcea10;
    --paper: #ffffff;
    --divider: #878787;
    --edge: #c8c8c8;
    --card-light: #f4f4f4;
    --card-shade: #d9d9d9;
  }
  * { margin: 0; padding: 0; box-sizing: border-box; }
  html, body { width: 900px; height: 1200px; overflow: hidden; background: var(--paper); }
  body { position: relative; font-family: "Arimo", Arial, sans-serif; }

  .card-side { position: absolute; left: 0; width: 900px; background: var(--ink); overflow: hidden; }
  .card-front { top: 0; height: 592px; }
  .card-back { top: 606px; height: 594px; }
  .divider { position: absolute; top: 592px; left: 0; width: 900px; height: 14px; background: var(--divider); }

  .band { position: absolute; top: 0; height: 100%; }
  .band-gold { background: var(--gold); }
  .band-white { background: var(--paper); }
  .card-front .band-gold { left: 820px; width: 25px; }
  .card-front .band-white { left: 845px; width: 55px; border-right: 1px solid var(--edge); }
  .card-back .band-white { left: 0; width: 55px; border-left: 1px solid var(--edge); }
  .card-back .band-gold { left: 55px; width: 23px; }

  .hand-art {
    position: absolute; left: 42px; top: 208px; width: 231px; height: 194px;
    background: linear-gradient(135deg, var(--card-light), var(--card-shade));
    border-radius: 10px;
  }

  .brand {
    position: absolute; left: 294px; width: 520px; top: 272px;
    text-align: center; color: var(--gold);
    font-size: 45px; line-height: 52px; font-weight: 400;
  }
  .tagline {
    position: absolute; left: 284px; width: 540px; top: 342px;
    text-align: center; color: var(--paper);
    font-size: 30px; line-height: 34px; font-variant: small-caps; letter-spacing: 0.3px;
  }

  .coach { position: absolute; right: 469px; top: 90px; text-align: right; }
  .coach-name { color: var(--gold); font-size: 46px; line-height: 52px; font-weight: 400; }
  .coach-role { color: var(--paper); font-size: 31px; line-height: 34px; }

  .contact {
    position: absolute; left: 559px; top: 420px; list-style: none;
    font-size: 22.7px; line-height: 31px; color: var(--paper);
  }
  .contact-label { color: var(--gold); }
</style>
</head>
<body>
  <section class="card-side card-front">
    <div class="hand-art" role="img" aria-label="Illustration of four aces fanned out in a hand"></div>
    <h1 class="brand">Ardmore Coaching</h1>
    <p class="tagline">Take Your Game To The Next Level</p>
    <div class="band band-gold"></div>
    <div class="band band-white"></div>
  </section>

  <div class="divider"></div>

  <section class="card-side card-back">
    <div class="band band-white"></div>
    <div class="band band-gold"></div>
    <div class="coach">
      <p class="coach-name">Callum Moray</p>
      <p class="coach-role">coaches</p>
    </div>
    <ul class="contact">
      <li><span class="contact-label">PH</span>: 555-555-5555</li>
      <li><span class="contact-label">WS</span>: www.mendmyhand.net</li>
      <li><span class="contact-label">EM</span>: emailaddress@email.com</li>
    </ul>
  </section>
</body>
</html>
```